Service business needs Business Card Design

Looking to create a new business card design that is both professional and unique the can highlight the many services we offer throughout the seasons. Our tagline is "The Cobalt Advantage"
Licensed & Insured: HC731462 has to be small and on the back side of the card.
On the Front:
FirstName LastName
Title
We offer the following services:
Deck Repair and Maintenance
Deck Cleaning and Staining/Painting
Power Washing/House Washing
Landscape Lighting Installation
Christmas Lighting Installation

```html
<!DOCTYPE html>
<html lang="en">
<head>
<meta charset="utf-8">
<title>Halvern Services – Business Card</title>
<link href="https://fonts.googleapis.com/css2?family=Arimo:ital,wght@0,400;0,700;1,700&display=swap" rel="stylesheet">
<style>
  :root {
    --backdrop: #e4e4e3;
    --card-white: #ffffff;
    --cobalt: #0a4c94;
    --cobalt-deep: #083f7d;
    --sky: #3db3e8;
    --ink-grey: #555a60;
    --paper-grey: #ececec;
  }
  * { box-sizing: border-box; margin: 0; padding: 0; }
  html, body { width: 1200px; height: 801px; overflow: hidden; }
  body {
    background: var(--backdrop);
    font-family: "Arimo", Arial, sans-serif;
    position: relative;
  }
  .card {
    position: absolute;
    top: 246px;
    width: 540px;
    height: 309px;
    overflow: hidden;
    box-shadow: 0 6px 18px rgba(0,0,0,0.18);
  }

  /* Front side */
  .card-front { left: 40px; background: var(--card-white); }
  .front-shade {
    position: absolute; right: 0; top: 0; width: 300px; height: 299px;
    background: linear-gradient(135deg, var(--paper-grey), #f6f6f6 70%, var(--card-white));
    border-bottom-left-radius: 0;
  }
  .front-band {
    position: absolute; left: 0; right: 0; bottom: 0; height: 10px;
    display: flex;
  }
  .front-band .band-deep { width: 48%; background: var(--cobalt); }
  .front-band .band-sky { flex: 1; background: var(--sky); }
  .brand {
    position: absolute; left: 34px; top: 52px;
    color: var(--cobalt);
    display: flex; align-items: center; gap: 10px;
  }
  .brand-dot { width: 22px; height: 22px; border-radius: 50%; background: var(--cobalt); }
  .brand-name { font-weight: 700; font-size: 34px; letter-spacing: 1px; line-height: 1; }
  .brand-sub { font-weight: 700; font-size: 13px; letter-spacing: 13px; line-height: 1; margin-top: 6px; }
  .person { position: absolute; left: 66px; top: 138px; }
  .person-name { color: var(--cobalt); font-weight: 700; font-size: 19px; letter-spacing: 0.5px; }
  .person-title { color: var(--ink-grey); font-size: 15px; margin-top: 2px; }
  .contacts { position: absolute; left: 66px; top: 200px; list-style: none; }
  .contacts li {
    display: flex; align-items: center; gap: 10px;
    color: var(--cobalt); font-size: 15px; line-height: 24px;
  }
  .contacts svg { width: 14px; height: 14px; fill: var(--cobalt); flex: none; }
  .address {
    position: absolute; right: 28px; top: 200px;
    color: var(--ink-grey); font-size: 14px; line-height: 18px; text-align: right;
  }

  /* Back side */
  .card-back {
    left: 620px; background: var(--cobalt);
    color: var(--card-white); text-align: center;
    display: flex; flex-direction: column; align-items: center; justify-content: center;
  }
  .card-back::before {
    content: ""; position: absolute; inset: 0;
    background: radial-gradient(ellipse at 70% 20%, rgba(61,179,232,0.35), transparent 60%);
  }
  .card-back > * { position: relative; }
  .back-brand { display: flex; align-items: center; gap: 12px; margin-bottom: 10px; }
  .back-brand .brand-dot { width: 24px; height: 24px; background: var(--card-white); }
  .back-brand .brand-name { font-size: 40px; }
  .back-brand .brand-sub { font-size: 14px; letter-spacing: 16px; }
  .services-lead { font-weight: 700; font-size: 14px; margin-bottom: 3px; }
  .services { list-style: none; font-size: 13px; line-height: 17px; }
  .license { font-size: 14px; margin-top: 10px; }
  .tagline { font-weight: 700; font-style: italic; font-size: 16px; margin-top: 4px; }
</style>
</head>
<body>
  <section class="card card-front">
    <div class="front-shade"></div>
    <div class="brand">
      <span class="brand-dot"></span>
      <div>
        <div class="brand-name">HALVERN</div>
        <div class="brand-sub">SERVICES</div>
      </div>
    </div>
    <div class="person">
      <div class="person-name">MARCUS DELANEY</div>
      <div class="person-title">Manager</div>
    </div>
    <ul class="contacts">
      <li><svg viewBox="0 0 24 24"><path d="M6.6 10.8a15.1 15.1 0 0 0 6.6 6.6l2.2-2.2c.3-.3.7-.4 1-.2 1.1.4 2.3.6 3.6.6.6 0 1 .4 1 1V20c0 .6-.4 1-1 1A17 17 0 0 1 3 4c0-.6.4-1 1-1h3.5c.6 0 1 .4 1 1 0 1.3.2 2.5.6 3.6.1.3 0 .7-.2 1z"/></svg>555-318-2740</li>
      <li><svg viewBox="0 0 24 24"><path d="M2 5h20v14H2zm2 2v.5l8 5 8-5V7l-8 5z"/></svg>contact@halvernpro.com</li>
      <li><svg viewBox="0 0 24 24"><circle cx="12" cy="12" r="10"/></svg>www.halvernpro.com</li>
    </ul>
    <div class="address">Your address, city<br>state, ZIP 0000</div>
    <div class="front-band"><span class="band-deep"></span><span class="band-sky"></span></div>
  </section>

  <section class="card card-back">
    <div class="back-brand">
      <span class="brand-dot"></span>
      <div>
        <div class="brand-name">HALVERN</div>
        <div class="brand-sub">SERVICES</div>
      </div>
    </div>
    <p class="services-lead">We offer the following services:</p>
    <ul class="services">
      <li>• Deck Repair and Maintenance</li>
      <li>• Deck Cleaning and Staining/Painting • Power Washing/House Washing</li>
      <li>• Landscape Lighting Installation • Christmas Lighting Installation</li>
    </ul>
    <p class="license">Licensed &amp; Insured: HC731462</p>
    <p class="tagline">The Cobalt Advantage</p>
  </section>
</body>
</html>
```